Quimby's Yard & Garden Center Business Card Update

I need an updated Business card design for my Lawn and Garden Center. We do Landscaping installs, Lawn Mowing, Snow Removal and also have a Garden Center Retail Division. I uploaded a few of our previous business cards to give an idea of what we are starting with. The main goal of this update is to simplify and modernize the business card, not all of the services that are on the previous cards has to be on the new one but I would still like to highlight our main services. There is also a sample of our logo that Can be used in the design.

Industry/Entity Type

Landscaping

Contact Information for Business Card

Morris Quimby
Morris@Quimbysyardandgarden.example
Business (555) 201-7784
Cell (555) 318-6092

Colors

Designer to choose colors to be used in the design.

Requirements
Must have
• Services Provided :
• Landscaping
• Lawn Maintenance
• Snow Removal
• Garden Center

```html
<!DOCTYPE html>
<html lang="en">
<head>
<meta charset="utf-8">
<title>Quimby's Yard &amp; Garden Center – Business Card</title>
<link rel="stylesheet" href="https://fonts.googleapis.com/css2?family=Montserrat:wght@500;600;700;800&display=swap">
<style>
  :root {
    --bg: #2b2b2b;
    --forest: #2d5a32;
    --forest-dark: #24482a;
    --pattern: #2a5230;
    --paper: #ffffff;
    --ink: #111111;
    --rule: #8a8a8a;
    --mark-grey: #c4c4c4;
    --bullet: #6e8d70;
  }
  * { box-sizing: border-box; margin: 0; padding: 0; }
  html, body { width: 1200px; height: 901px; overflow: hidden; }
  body {
    background: var(--bg);
    font-family: "Montserrat", Arial, sans-serif;
    color: var(--ink);
    position: relative;
  }
  .card {
    position: absolute;
    left: 267px;
    width: 665px;
    height: 380px;
    overflow: hidden;
  }
  /* Back side */
  .card-back { top: 40px; background: var(--forest); }
  .card-back .pattern-fill {
    position: absolute; inset: 0;
    background: linear-gradient(135deg, var(--forest) 0%, var(--pattern) 100%);
  }
  .card-back .back-name {
    position: absolute; right: 70px; bottom: 58px;
    font-weight: 800; font-size: 22px; color: var(--mark-grey);
  }
  /* Front side */
  .card-front { top: 470px; background: var(--paper); }
  .brand {
    position: absolute; left: 40px; top: 140px; width: 270px;
    display: flex; align-items: center; gap: 12px;
  }
  .brand-square { width: 26px; height: 26px; background: var(--forest); flex: none; }
  .brand-name { font-weight: 800; font-size: 40px; color: var(--forest); }
  .divider {
    position: absolute; left: 325px; top: 92px; width: 2px; height: 160px;
    background: var(--rule);
  }
  .contact { position: absolute; left: 348px; top: 82px; width: 280px; }
  .contact-name { font-weight: 800; font-size: 26px; line-height: 1.05; }
  .contact-title {
    font-weight: 700; font-size: 15px; color: var(--forest);
    margin-top: 1px;
  }
  .contact-address {
    font-weight: 600; font-size: 12.5px; letter-spacing: 0.5px;
    margin-top: 8px; padding-bottom: 7px;
    border-bottom: 2px solid var(--rule); width: 245px;
  }
  .contact-list { list-style: none; margin-top: 12px; }
  .contact-list li {
    display: flex; align-items: center; gap: 10px;
    font-weight: 600; font-size: 13px; letter-spacing: 1.2px;
    height: 24px; white-space: nowrap;
  }
  .contact-list li.email { font-size: 11px; letter-spacing: 0.3px; margin-top: 4px; }
  .contact-list svg { width: 16px; height: 16px; flex: none; fill: var(--forest); }
  .band-line {
    position: absolute; left: 0; right: 0; top: 294px; height: 12px;
    background: var(--forest);
  }
  .services-strip {
    position: absolute; left: 0; right: 0; top: 306px; height: 42px;
    background: var(--paper);
    display: flex; align-items: center; padding-left: 120px;
    font-weight: 700; font-size: 12.5px; letter-spacing: 1px;
    color: var(--ink); white-space: nowrap;
  }
  .services-strip span::before { content: "•"; margin: 0 4px; color: var(--bullet); }
  .services-strip span:first-child::before { margin-left: 0; }
  .band-bottom {
    position: absolute; left: 0; right: 0; top: 348px; height: 22px;
    background: var(--forest);
  }
</style>
</head>
<body>
  <section class="card card-back" aria-label="Card back">
    <div class="pattern-fill" role="img" aria-label="Repeating pattern of small tree shapes in darker green"></div>
    <div class="back-name">Quimby's</div>
  </section>

  <section class="card card-front" aria-label="Card front">
    <div class="brand">
      <span class="brand-square"></span>
      <span class="brand-name">Quimby's</span>
    </div>
    <div class="divider"></div>
    <div class="contact">
      <div class="contact-name">Morris Quimby</div>
      <div class="contact-title">Director</div>
      <div class="contact-address">Your Street Address,</div>
      <ul class="contact-list">
        <li>
          <svg viewBox="0 0 16 16" aria-hidden="true"><path d="M4 1h8a1 1 0 0 1 1 1v12a1 1 0 0 1-1 1H4a1 1 0 0 1-1-1V2a1 1 0 0 1 1-1zm1 2v9h6V3H5zm3 10a.8.8 0 1 0 0 1.6A.8.8 0 0 0 8 13z"/></svg>
          (555) 201-7784
        </li>
        <li>
          <svg viewBox="0 0 16 16" aria-hidden="true"><path d="M1 5c0-2 3-3 7-3s7 1 7 3v1h-3V5H4v1H1V5zm3 2h8l2 7H2l2-7zm2 2v1h1V9H6zm3 0v1h1V9H9zm-3 2v1h1v-1H6zm3 0v1h1v-1H9z"/></svg>
          (555) 318-6092
        </li>
        <li class="email">
          <svg viewBox="0 0 16 16" aria-hidden="true"><path d="M1 3h14v10H1V3zm1.5 1.2L8 8.6l5.5-4.4h-11zM2 5.3V12h12V5.3L8 10 2 5.3z"/></svg>
          Morris@Quimbysyardandgarden.example
        </li>
      </ul>
    </div>
    <div class="band-line"></div>
    <div class="services-strip">
      <span>Landscaping</span><span>Law Maintenance</span><span>Snow Removal</span><span>Garden Center</span>
    </div>
    <div class="band-bottom"></div>
  </section>
</body>
</html>
```